Business Card Design

Tallgrove Holdings Pty Ltd is a builder and developer of quality homes that may include , lifestyle , prestige and other affordable homes. We design ,customise and build turn key homes to 6 star energy ratings.

Reason: So far the card designs I have received do not show me what I need to see on it. The information on the card must have the following information only: Name : Marek Holloway Company Name : TallGrove Holding's Pty Ltd Phone number : 0492 305 718 Email address: marekholloway@quillnet.example.au Business address: 47 Brindlecombe Court , Rowville, Vic 3999 Company Logo : You need to design this logo and then design the business card and place the logo on the card appropriately. At the moment non are acceptable to me for reasons shown above. Give me a stand alone logo separately and on the designed business card Dead line is extended to 15 October 2015. Feel welcome to call me +61 492 305 718 to discuss and clarify the relevant information if required

Industry/Entity Type

Business

Contact Information for Business Card

Marek Holloway
marekholloway@quillnet.example.au
Mobile : +61 492305718

```html
<!DOCTYPE html>
<html lang="en">
<head>
<meta charset="utf-8">
<title>Tallgrove Holdings Pty Ltd – Business Card</title>
<link rel="stylesheet" href="https://fonts.googleapis.com/css2?family=Montserrat:wght@500;600&family=Exo+2:wght@600&display=swap">
<style>
  :root {
    --ink: #000000;
    --brand-blue: #1f86d6;
    --stripe-blue: #1a6fb5;
    --white: #ffffff;
  }
  * { margin: 0; padding: 0; box-sizing: border-box; }
  html, body { width: 741px; height: 1200px; overflow: hidden; background: var(--ink); }
  .card { position: relative; width: 741px; height: 1200px; background: var(--ink); font-family: "Montserrat", sans-serif; color: var(--white); }

  .brand-mark { position: absolute; left: 280px; top: 30px; width: 180px; height: 180px; border-radius: 50%; background: var(--brand-blue); }
  .brand-name { position: absolute; top: 212px; left: 0; width: 100%; text-align: center; font-weight: 600; font-size: 76px; color: var(--brand-blue); letter-spacing: 2px; line-height: 1; }
  .company-line { position: absolute; top: 300px; left: 0; width: 100%; text-align: center; font-weight: 600; font-size: 54px; color: var(--white); line-height: 1; }

  .side-bar { position: absolute; top: 480px; height: 315px; }
  .side-bar.blue-left { left: 0; width: 54px; background: var(--brand-blue); }
  .side-bar.white-left { left: 54px; width: 45px; background: var(--white); }
  .side-bar.white-right { left: 642px; width: 45px; background: var(--white); }
  .side-bar.blue-right { left: 687px; width: 54px; background: var(--brand-blue); }

  .name-panel { position: absolute; left: 99px; top: 480px; width: 543px; height: 220px; background: var(--ink); display: flex; align-items: center; justify-content: center; font-family: "Exo 2", sans-serif; color: var(--brand-blue); }
  .person-name { font-size: 52px; letter-spacing: 3px; font-weight: 600; line-height: 1; white-space: nowrap; }

  .stripe-band { position: absolute; left: 99px; top: 700px; width: 543px; height: 95px; background: linear-gradient(180deg, var(--stripe-blue), var(--brand-blue)); }

  .contact-panel { position: absolute; left: 0; top: 795px; width: 741px; height: 285px; background: var(--ink); }
  .contact-row { position: absolute; left: 122px; display: flex; align-items: center; gap: 34px; }
  .contact-row svg { width: 76px; height: 76px; flex: none; }
  .contact-text { font-size: 24px; font-weight: 500; letter-spacing: 1px; white-space: nowrap; line-height: 1.3; }
  .row-phone { top: 22px; }
  .row-email { top: 106px; }
  .row-address { top: 190px; }

  .footer-band { position: absolute; left: 0; top: 1080px; width: 741px; height: 120px; background: linear-gradient(180deg, var(--brand-blue), var(--stripe-blue)); }
</style>
</head>
<body>
<main class="card">
  <div class="brand-mark" role="img" aria-label="Tallgrove Holdings brand mark"></div>
  <div class="brand-name">TALLGROVE</div>
  <div class="company-line">Holdings Pty Ltd</div>

  <div class="side-bar blue-left"></div>
  <div class="side-bar white-left"></div>
  <div class="side-bar white-right"></div>
  <div class="side-bar blue-right"></div>

  <section class="name-panel">
    <span class="person-name">Marek Holloway</span>
  </section>

  <div class="stripe-band" role="img" aria-label="Blue vertical stripe pattern"></div>

  <section class="contact-panel">
    <div class="contact-row row-phone">
      <svg viewBox="0 0 76 76" aria-hidden="true">
        <circle cx="38" cy="38" r="34" fill="none" stroke="#fff" stroke-width="4"/>
        <path d="M27 22 l7 -2 l5 11 l-5 4 q3 8 10 12 l4 -5 l11 5 l-2 7 q-4 4 -10 2 q-16 -6 -22 -22 q-2 -7 2 -12 z" fill="#fff"/>
      </svg>
      <span class="contact-text">+61 492305718</span>
    </div>
    <div class="contact-row row-email">
      <svg viewBox="0 0 76 76" aria-hidden="true">
        <circle cx="38" cy="38" r="34" fill="none" stroke="#fff" stroke-width="4"/>
        <rect x="20" y="26" width="36" height="25" rx="2" fill="#fff"/>
        <path d="M21 28 L38 41 L55 28" fill="none" stroke="#000" stroke-width="3"/>
      </svg>
      <span class="contact-text">marekholloway@quillnet.example.au</span>
    </div>
    <div class="contact-row row-address">
      <svg viewBox="0 0 76 76" aria-hidden="true">
        <circle cx="38" cy="38" r="34" fill="none" stroke="#fff" stroke-width="4"/>
        <path d="M38 57 C30 46 25 40 25 33 a13 13 0 0 1 26 0 c0 7 -5 13 -13 24 z" fill="#fff"/>
        <circle cx="38" cy="33" r="5" fill="#000"/>
      </svg>
      <span class="contact-text">47 Brindlecombe Court,<br>Rowville, Vic 3999</span>
    </div>
  </section>

  <div class="footer-band" role="img" aria-label="Blue vertical stripe pattern"></div>
</main>
</body>
</html>
```